依頼詳細
アプリを新規インストールやバージョンアップした後、
初めて起動する際に表示されるチュートリアル画面の画像4枚の作成依頼です。
仕様する画像は、イラスト、写真画像、アニメなど指定はありません。

文言は既に決まっておりますので、
各文言にあうデザインを入れて作成したものをお待ちしております。
※イメージ画像はファイル添付しております。

画像サイズはこちらで調整しますので、大きいもので問題ありません。
アプリで使用しますので、縦横比はご考慮ください。
記載項目
下記文言はそのまま使用してください。
(添付ファイル参照・画像はサンプルで入れているだけですので自由にデザインをお願いします)
・使わなくなったもの ミルタスであげよう!もらおう!
・撮って出して取りに来る 捨てる時代から繋げる時代へ
ミルタスは地球からゴミがなくなることを目指します
・欲しいものはリクエスト 買わなくても譲ってもらえる
・出品無料!会員登録ももちろん無料!

サイズ
• スマホで表示される縦長で。縦横比は機種により異なるため、こちらで調整します。大きいサイズでも可。
希望イメージ
シンプル 複雑
単色 カラフル
暗い 明るい
日常 高級
遊び心 厳粛
未来的 伝統的
女性的 男性的
希望する色
青系
納品ファイル
• 高解像度JPG (.jpg)
• イラストレーター形式 (.ai)
• フォトショップ形式 (.psd)
補足説明
■ 選んだ理由

シンプルですっきりしていますが、
サイトイメージに合った画像の使い方や色使いに目を引き、
採用させていただきました。

何度も細かな修正に迅速にご対応いただき、大変感謝しております。
また機会がありましたら、是非ご依頼させていただきたいと思います。

■ 提案者全員のお礼・コメント

皆様、様々なアイデアや素晴らしいご提案をいただき、
ありがとうございました。
また機会がありましたら是非よろしくお願いいたします。

```html
<!DOCTYPE html>
<html lang="ja">
<head>
<meta charset="utf-8">
<title>ミルタス チュートリアル 2</title>
<link rel="stylesheet" href="https://fonts.googleapis.com/css2?family=Noto+Sans+JP:wght@400;500&display=swap">
<style>
  :root {
    --page-bg: #ffffff;
    --card-teal: #2fd3cf;
    --ink-navy: #1f2a4d;
    --dot-white: #ffffff;
    --button-line: #ffffff;
    --photo-warm: #c79a6b;
    --photo-navy: #1c2b5a;
    --hand-skin: #f6dcc8;
  }
  html, body {
    margin: 0;
    padding: 0;
    width: 675px;
    height: 1200px;
    overflow: hidden;
    background: var(--page-bg);
    font-family: "Noto Sans JP", sans-serif;
  }
  .tutorial-card {
    position: absolute;
    left: 32px;
    top: 63px;
    width: 612px;
    height: 1073px;
    background: var(--card-teal);
    border-radius: 14px;
  }
  .hero-illustration {
    position: absolute;
    left: 70px;
    top: 40px;
    width: 480px;
    height: 590px;
    border-radius: 40px;
    background: linear-gradient(160deg, var(--photo-navy) 0%, var(--photo-warm) 55%, var(--hand-skin) 100%);
    opacity: 0.9;
  }
  .headline {
    position: absolute;
    left: 0;
    top: 690px;
    width: 100%;
    margin: 0;
    text-align: center;
    color: var(--ink-navy);
    font-size: 33px;
    font-weight: 500;
    line-height: 52px;
    letter-spacing: 1px;
  }
  .mission {
    position: absolute;
    left: 110px;
    top: 810px;
    width: 420px;
    margin: 0;
    color: var(--ink-navy);
    font-size: 23px;
    font-weight: 400;
    line-height: 32px;
  }
  .page-dots {
    position: absolute;
    left: 0;
    top: 906px;
    width: 100%;
    display: flex;
    justify-content: center;
    gap: 27px;
  }
  .page-dots span {
    width: 18px;
    height: 18px;
    border-radius: 50%;
    background: var(--dot-white);
  }
  .page-dots .is-current { background: var(--ink-navy); }
  .next-button {
    position: absolute;
    left: 209px;
    top: 963px;
    width: 194px;
    height: 44px;
    box-sizing: border-box;
    border: 2px solid var(--button-line);
    border-radius: 22px;
    color: var(--button-line);
    font-size: 21px;
    line-height: 40px;
    text-align: center;
  }
</style>
</head>
<body>
  <section class="tutorial-card">
    <div class="hero-illustration" role="img" aria-label="手に持ったスマートフォンで雑貨の写真を撮影しているイラスト、画面中央にカメラアイコン"></div>
    <h1 class="headline">撮って出して取りに来る<br>捨てる時代から繋げる時代へ</h1>
    <p class="mission">ミルタスは地球からゴミがなくなることを目指します</p>
    <div class="page-dots">
      <span></span><span class="is-current"></span><span></span><span></span>
    </div>
    <div class="next-button">次へ</div>
  </section>
</body>
</html>
```